Wine label refresh

We are wanting to modify our Corran Estate label to include a picture on it.
I have attached the pictures below which we would like on the label. They are of the Corran Estate vineyard. I have also attached an example of another label with a picture on it that we like the style of.
Industry/Entity Type
Vineyard
Requirements
Must have
- The Corran Estate text must stay the same but can be moved down. It still needs to be the same size though.
Marlborough Sauvignon Blanc should remain in the same font and roughly the same size.
Wine of New Zealand also must stay but could potentially be moved.
Nice to have
- It would be nice if we could keep the KL logo on the front label but feel free to experiment with where this goes.

```html
<!DOCTYPE html>
<html lang="en">
<head>
<meta charset="utf-8">
<title>Corran Estate – Marlborough Sauvignon Blanc Label</title>
<link rel="stylesheet" href="https://fonts.googleapis.com/css2?family=Cormorant+Garamond:ital,wght@0,500;1,500&family=Pinyon+Script&family=Tenor+Sans&display=swap">
<style>
  :root {
    --backdrop: #211f1f;
    --gold: #c9a56a;
    --gold-deep: #b88f4e;
    --paper: #ffffff;
    --ink: #1d1d1d;
    --script-ink: #2f3a22;
    --muted: #8d8d8d;
    --sky-top: #9fb0c4;
    --sky-low: #dfe5ea;
    --hills: #8c9a6e;
    --vines: #4f7a2e;
    --grass: #6aa23c;
  }

  * { box-sizing: border-box; margin: 0; padding: 0; }

  html, body {
    width: 1200px;
    height: 900px;
    overflow: hidden;
    background: var(--backdrop);
  }

  .canvas {
    position: relative;
    width: 1200px;
    height: 900px;
  }

  .wine-label {
    position: absolute;
    left: 170px;
    top: 63px;
    width: 860px;
    height: 774px;
    background: var(--gold);
    padding: 25px;
  }

  .label-paper {
    position: relative;
    width: 100%;
    height: 100%;
    background: var(--paper);
  }

  .label-paper::before {
    content: "";
    position: absolute;
    inset: 6px;
    border: 3px solid var(--gold);
    pointer-events: none;
  }

  .monogram {
    position: absolute;
    left: 0;
    right: 0;
    top: 22px;
    text-align: center;
    font-family: "Cormorant Garamond", serif;
    font-weight: 500;
    font-size: 84px;
    line-height: 1;
    letter-spacing: 2px;
    color: var(--gold-deep);
  }

  .estate-name {
    position: absolute;
    left: 0;
    right: 0;
    top: 138px;
    text-align: center;
    font-family: "Cormorant Garamond", serif;
    font-weight: 500;
    font-size: 62px;
    line-height: 1;
    font-variant: small-caps;
    letter-spacing: 3px;
    color: var(--ink);
  }

  .vineyard-photo {
    position: absolute;
    left: 47px;
    top: 213px;
    width: 715px;
    height: 324px;
    background: linear-gradient(
      to bottom,
      var(--sky-top) 0%,
      var(--sky-low) 30%,
      var(--hills) 42%,
      var(--vines) 58%,
      var(--grass) 80%,
      var(--vines) 100%
    );
  }

  .varietal {
    position: absolute;
    left: 0;
    right: 0;
    top: 560px;
    text-align: center;
    font-family: "Pinyon Script", cursive;
    font-size: 46px;
    line-height: 1;
    color: var(--script-ink);
  }

  .vintage {
    position: absolute;
    left: 0;
    right: 0;
    top: 612px;
    text-align: center;
    font-family: "Cormorant Garamond", serif;
    font-style: italic;
    font-weight: 500;
    font-size: 38px;
    line-height: 1;
    color: var(--script-ink);
  }

  .label-footer {
    position: absolute;
    left: 22px;
    right: 22px;
    top: 666px;
    display: flex;
    justify-content: space-between;
    align-items: baseline;
    font-family: "Tenor Sans", sans-serif;
    font-size: 27px;
    line-height: 1;
    color: var(--muted);
  }
</style>
</head>
<body>
  <main class="canvas">
    <section class="wine-label" aria-label="Corran Estate Marlborough Sauvignon Blanc front label">
      <div class="label-paper">
        <div class="monogram">KL</div>
        <h1 class="estate-name">Corran Estate</h1>
        <div class="vineyard-photo" role="img" aria-label="Photograph of the Corran Estate vineyard: rows of vines, palm trees and a homestead beneath green hills and a cloudy sky"></div>
        <p class="varietal">Marlborough Sauvignon Blanc</p>
        <p class="vintage">2012</p>
        <div class="label-footer">
          <span class="volume">750ml</span>
          <span class="origin">NEW ZEALAND WINE</span>
          <span class="strength">13% alc/vol</span>
        </div>
      </div>
    </section>
  </main>
</body>
</html>
```